Very clean, very simple business card needed.

I am looking for a VERY simple business card. I have attached our logo. I would like it to be a mainly white card. I have picked double sided but would be open to single as well. I want the overall feel to be simple, classic, and professional. Thank you.

Industry/Entity Type

Consultant

Contact Information for Business Card

Dennis Pellowe

862 North Larchmere Avenue, Summit Floor, Brookmere Falls, Wisconsin 60719
denny@hollisterbaycapital.example
www.hollisterbaycapital.example

Font styles to use
Serif

Colors

Designer to choose colors to be used in the design.

Requirements
Must have
• The business card details and in an editable form to change the names and emails of employees easily.
Nice to have
• n/a
Should not have
• Pictures, big lines and stripes, too much color.

```html
<!DOCTYPE html>
<html lang="en">
<head>
<meta charset="utf-8">
<title>Hollister Bay Capital – Business Card</title>
<link href="https://fonts.googleapis.com/css2?family=Tinos:wght@400&display=swap" rel="stylesheet">
<style>
  :root {
    --brand-indigo: #362f85;
    --card-white: #ffffff;
    --stage-grey: #e6e6ea;
    --ink-white: #f4f3fb;
    --ink-soft: #d9d6f0;
  }
  * { box-sizing: border-box; margin: 0; padding: 0; }
  html, body {
    width: 1200px; height: 660px; overflow: hidden;
    background: var(--stage-grey);
    font-family: "Tinos", "Times New Roman", serif;
  }
  .stage {
    width: 1200px; height: 660px;
    display: flex; align-items: center; justify-content: center; gap: 40px;
  }
  .card {
    width: 540px; height: 309px;
    position: relative;
    box-shadow: 0 6px 18px rgba(0,0,0,.18);
  }
  .card--back { background: var(--brand-indigo); display: flex; align-items: center; justify-content: center; }
  .card--front { background: var(--card-white); }

  .brand { display: flex; align-items: center; gap: 12px; }
  .brand__square { width: 22px; height: 22px; flex: none; }
  .brand__name {
    font-size: 21px; letter-spacing: 1.5px; text-transform: uppercase; white-space: nowrap;
  }
  .card--back .brand__square { background: var(--card-white); }
  .card--back .brand__name { color: var(--card-white); }
  .card--front .brand__square { background: var(--brand-indigo); }
  .card--front .brand__name { color: var(--brand-indigo); font-size: 17px; }

  .front__logo-zone {
    position: absolute; left: 0; top: 0; width: 306px; height: 100%;
    display: flex; align-items: center; justify-content: center;
  }
  .front__panel {
    position: absolute; top: 12px; right: 12px; bottom: 12px; width: 222px;
    background: var(--brand-indigo); color: var(--ink-white);
    padding: 40px 18px 22px 22px;
    display: flex; flex-direction: column; justify-content: space-between;
  }
  .person__name { font-size: 15px; letter-spacing: 1.6px; text-transform: uppercase; }
  .person__title { font-size: 11.5px; color: var(--ink-soft); margin-top: 3px; }
  .contact { font-size: 11px; line-height: 1.5; font-style: normal; }
  .contact__web { margin-bottom: 8px; }
</style>
</head>
<body>
<main class="stage">
  <section class="card card--back" aria-label="Card back">
    <div class="brand">
      <span class="brand__square"></span>
      <span class="brand__name">Hollister Bay Capital</span>
    </div>
  </section>

  <section class="card card--front" aria-label="Card front">
    <div class="front__logo-zone">
      <div class="brand">
        <span class="brand__square"></span>
        <span class="brand__name">Hollister Bay Capital</span>
      </div>
    </div>
    <div class="front__panel">
      <div class="person">
        <p class="person__name">Dennis Pellowe</p>
        <p class="person__title">Founder and Principal</p>
      </div>
      <address class="contact">
        <p>denny@hollisterbaycapital.example</p>
        <p class="contact__web">www.hollisterbaycapital.example</p>
        <p>862 North Larchmere Avenue</p>
        <p>Summit Floor</p>
        <p>Brookmere Falls, Wisconsin 60719</p>
      </address>
    </div>
  </section>
</main>
</body>
</html>
```